Skincare Cleanser Bottle Label

New product launch of a mint facial cleanser.
Brand is called Dorvella.
Product will be called Lumora.
Looking for a label design that can be printed using silk screening.
High gloss white plastic bottle. 8oz. White push pump top.
Clinical skincare brand, professional image, sold in medical spas.

Target Market(s)

Women Age 20-65

Industry/Entity Type

Health And Wellness

Font styles to use
Serif
Sans Serif

Requirements
Must have
• Dorvella brand name in the orignal font.
Should not have
• Multiple colours.

```html
<!DOCTYPE html>
<html lang="en">
<head>
<meta charset="utf-8">
<title>Dorvella Lumora – Mint Facial Cleanser Label</title>
<link rel="stylesheet" href="https://fonts.googleapis.com/css2?family=Roboto+Slab:wght@300&family=Fira+Sans:ital,wght@0,300;1,300;1,400&display=swap">
<style>
  :root {
    --backdrop: #f4f4f4;
    --label: #ffffff;
    --ink: #1a1a1a;
    --rule: #8a8a8a;
    --reverse: #ffffff;
    --mint-deep: #2f8a2a;
    --mint-light: #6cc24a;
  }
  * { margin: 0; padding: 0; box-sizing: border-box; }
  html, body {
    width: 900px;
    height: 1200px;
    overflow: hidden;
    background: var(--backdrop);
  }
  .canvas {
    position: relative;
    width: 900px;
    height: 1200px;
  }
  .label {
    position: absolute;
    left: 310px;
    top: 260px;
    width: 280px;
    height: 820px;
    background: var(--label);
    border-radius: 6px;
  }
  .brand-name {
    position: absolute;
    left: 398px;
    top: 690px;
    transform: translate(-50%, -50%) rotate(-90deg);
    font-family: "Roboto Slab", serif;
    font-weight: 300;
    font-size: 66px;
    letter-spacing: 2px;
    line-height: 1;
    color: var(--ink);
    white-space: nowrap;
  }
  .mint-photo {
    position: absolute;
    left: 388px;
    top: 410px;
    width: 88px;
    height: 80px;
    border-radius: 50%;
    background: radial-gradient(circle at 45% 40%, var(--mint-light), var(--mint-deep));
  }
  .product-tab {
    position: absolute;
    left: 430px;
    top: 498px;
    width: 92px;
    height: 220px;
  }
  .product-name {
    position: absolute;
    left: 472px;
    top: 604px;
    transform: translate(-50%, -50%) rotate(-90deg);
    font-family: "Fira Sans", sans-serif;
    font-style: italic;
    font-weight: 300;
    font-size: 52px;
    letter-spacing: 2px;
    line-height: 1;
    color: var(--reverse);
    white-space: nowrap;
  }
  .product-type {
    position: absolute;
    left: 505px;
    top: 580px;
    transform: translate(-50%, -50%) rotate(-90deg);
    font-family: "Fira Sans", sans-serif;
    font-style: italic;
    font-weight: 400;
    font-size: 11px;
    line-height: 1;
    color: var(--reverse);
    white-space: nowrap;
  }
  .tagline {
    position: absolute;
    left: 364px;
    top: 956px;
    width: 122px;
    padding: 4px 0 3px;
    border-top: 1.5px solid var(--rule);
    border-bottom: 1.5px solid var(--rule);
    font-family: "Fira Sans", sans-serif;
    font-weight: 300;
    font-size: 20px;
    line-height: 1.1;
    color: var(--ink);
    text-align: center;
  }
  .volume {
    position: absolute;
    left: 373px;
    top: 995px;
    font-family: "Fira Sans", sans-serif;
    font-weight: 300;
    font-size: 17px;
    color: var(--ink);
  }
  .volume em { font-style: italic; }
</style>
</head>
<body>
  <main class="canvas">
    <section class="label"></section>

    <div class="brand-name">dorvella</div>

    <div class="mint-photo" role="img" aria-label="Photo of a fresh green mint sprig"></div>

    <svg class="product-tab" viewBox="0 0 92 220" aria-hidden="true">
      <path d="M4 220 L4 30 Q4 4 30 4 L70 4 Q90 4 90 24 L90 170 Q90 214 50 218 Z" fill="#1a1a1a"/>
    </svg>
    <div class="product-name">lumora</div>
    <div class="product-type">mint facial cleanser</div>

    <div class="tagline">lorem ipsum</div>
    <div class="volume">250 <em>ml</em></div>
  </main>
</body>
</html>
```